Corporate Brightfen business cards to be handed to investor, bankers etc. Needs to have a young feel

I need business cards designed for a technology company that provides uber-like rapid response on the security industry. I would like it simple but very cool and tasteful. See attached documents for artwork and colours to be used. Cut sheet describes business model. Card stock should be thicker than normal. I would like the one side to be just the art and the other to have the contact info with maybe the pin somewhere.

Target Market(s)

Investors

Industry/Entity Type

Business

Contact Information for Business Card

Would like the logo attached on one side with name address and other info on the other side.

Font styles to use
Other font styles liked:
• See existing logo

Colors
6b449b
886aae
e4daeb
ffffff

Requirements
Must have
• Name: Dorian Felkatsis
• Address: 47 Larkfield Avenue, Toronto, On, M6K2B7
• Tel: 416-7291846
• Email: rolo@brightfen.io
Nice to have
• See logo colours

```html
<!DOCTYPE html>
<html lang="en">
<head>
<meta charset="utf-8">
<title>Dorian Felkatsis — Brightfen business card</title>
<link rel="stylesheet" href="https://fonts.googleapis.com/css2?family=Exo+2:wght@300;400&display=swap">
<style>
  :root {
    --paper: #ffffff;
    --ink-deep: #3b0b55;
    --ink-soft: #9266b6;
    --tone-pale: #efe7f3;
    --tone-light: #c9b3dd;
    --tone-mid: #8a62b8;
    --tone-deep: #5f1f95;
  }
  html, body {
    margin: 0;
    padding: 0;
    overflow: hidden;
    background: var(--paper);
  }
  .card {
    position: relative;
    width: 1200px;
    height: 685px;
    background: var(--paper);
    overflow: hidden;
    font-family: "Exo 2", sans-serif;
  }
  .card__art {
    position: absolute;
    inset: 0;
    width: 1200px;
    height: 685px;
  }
  .card__name {
    position: absolute;
    right: 67px;
    top: 46px;
    margin: 0;
    font-weight: 400;
    font-size: 70px;
    letter-spacing: 2px;
    color: var(--ink-deep);
    line-height: 1;
  }
  .contact {
    position: absolute;
    display: flex;
    align-items: flex-start;
    gap: 18px;
    color: var(--ink-soft);
    font-weight: 300;
    letter-spacing: 1px;
  }
  .contact__icon {
    flex: none;
    width: 44px;
    height: 44px;
  }
  .contact__icon circle { fill: var(--ink-deep); }
  .contact__icon .glyph { fill: var(--paper); }
  .contact__text { margin: 0; }
  .contact--address { left: 528px; top: 218px; font-size: 36px; line-height: 47px; }
  .contact--email { left: 574px; top: 396px; font-size: 38px; line-height: 44px; gap: 12px; }
  .contact--phone { left: 569px; top: 530px; font-size: 41px; line-height: 48px; gap: 12px; }
</style>
</head>
<body>
  <div class="card">
    <svg class="card__art" viewBox="0 0 753 430" preserveAspectRatio="none" role="img" aria-label="Abstract layered purple artwork sweeping in from the left edge">
      <defs>
        <radialGradient id="art-tone" cx="0.12" cy="0.1" r="1.05">
          <stop offset="0" stop-color="var(--tone-deep)"/>
          <stop offset="0.45" stop-color="var(--tone-mid)"/>
          <stop offset="0.8" stop-color="var(--tone-light)"/>
          <stop offset="1" stop-color="var(--tone-pale)"/>
        </radialGradient>
      </defs>
      <path fill="url(#art-tone)" d="M0 0 H330 C420 100 470 250 475 430 H0Z"/>
    </svg>

    <h1 class="card__name">Dorian Felkatsis</h1>

    <div class="contact contact--address">
      <svg class="contact__icon" viewBox="0 0 44 44" aria-hidden="true">
        <circle cx="22" cy="22" r="21"/>
        <path class="glyph" d="M22 10 C16.5 10 13 14 13 18.5 C13 24.5 22 34 22 34 C22 34 31 24.5 31 18.5 C31 14 27.5 10 22 10Z M22 15 A3.6 3.6 0 1 1 21.99 15Z"/>
      </svg>
      <p class="contact__text">47 Larkfield Avenue, Toronto,<br>On, M6K2B7</p>
    </div>

    <div class="contact contact--email">
      <svg class="contact__icon" viewBox="0 0 44 44" aria-hidden="true">
        <circle cx="22" cy="22" r="21"/>
        <path class="glyph" d="M11 14 H33 V30 H11Z"/>
        <path d="M11.5 14.5 L22 23 L32.5 14.5" fill="none" stroke="var(--ink-deep)" stroke-width="2"/>
      </svg>
      <p class="contact__text">rolo@brightfen.io</p>
    </div>

    <div class="contact contact--phone">
      <svg class="contact__icon" viewBox="0 0 44 44" aria-hidden="true">
        <circle cx="22" cy="22" r="21"/>
        <path class="glyph" d="M15 11 L19 11 L21 17 L18 19 C19.5 22.5 21.5 24.5 25 26 L27 23 L33 25 L33 29 C33 31 31.5 32 29.5 32 C20 31 13 24 12 14.5 C12 12.5 13 11 15 11Z"/>
      </svg>
      <p class="contact__text">416-7291846</p>
    </div>
  </div>
</body>
</html>
```